EB-5 Regional Center needs a Web design

Marlowfield Equity Partners is an expanding EB-r regional center. We have been successful in sponsoring multiple projects of third-party developers and placing EB-5, B-1, and Private Investments into multiple projects.

We are now partnering directly with project developers in the energy and healthcare to raise foreign capital for projects in those industries. The foreign capital is used as project equity and our collective balance sheets are used to guarantee debt to complete the funding of the projects.

We need a web site where we can post our company credentials, the bios of each partner, a document page for each of our projects where we can post specific project related documents which foreign investors can read, and we will need a section where foreign investors can fill out investor forms confirming that they are qualified investors and leaving their contact so that our agents and executives can make contact.

The final design should reflect the exceptional experience of the partners and our financial strength and stability.

We do have a logo we would want to use on the web design.

Target Market(s)

EB-5 Investors, B-1 Investors, Private Equity and other investors seeking quality investment in job creating US projects.

Coding

Coded - Design and coding required

Number of Pages Required

5+ page

Font styles to use
Sans Serif

Requirements
Must have
• Pages to display company info, partner bios, projects completed, and a projects in-process page where we can post documents and info on projects for which we are seeking foreign investment. We also need a section where investors can enter their qualifying personal information and leave contact information for us.

```html
<!DOCTYPE html>
<html lang="en">
<head>
<meta charset="utf-8">
<title>Marlowfield Equity Partners</title>
<link href="https://fonts.googleapis.com/css2?family=Poppins:wght@300;400;500;600;700;800&display=swap" rel="stylesheet">
<style>
:root{
  --blue:#1f4fd8;
  --blue-dark:#1a37b8;
  --blue-light:#3b82f0;
  --ink:#111111;
  --text:#555b66;
  --muted:#7a808a;
  --grey-bg:#f7f7f7;
  --footer:#080808;
  --white:#ffffff;
}
*{box-sizing:border-box;margin:0;padding:0}
html,body{width:1200px;height:4078px;overflow:hidden}
body{position:relative;font-family:'Poppins',sans-serif;color:var(--text);background:var(--white)}
.abs{position:absolute}
.center{text-align:center}

/* hero */
.hero{left:0;top:0;width:1200px;height:772px;background:linear-gradient(180deg,#3c4552 0%,#27313d 45%,#1d2a3a 100%)}
.hero-cut{left:0;top:640px;width:1200px;height:140px}
.brand{display:flex;align-items:center;gap:12px;color:var(--white);font-weight:600;font-size:24px;letter-spacing:.5px}
.brand .dot{width:16px;height:16px;border-radius:50%;background:var(--white)}
.nav{right:112px;top:36px;display:flex;gap:26px;font-size:14px;color:var(--white);align-items:center}
.nav .active{color:#5a8cff;border-bottom:2px solid #5a8cff;padding-bottom:4px;margin-top:6px}
.hero-title{left:0;width:1200px;top:282px;font-size:50px;font-weight:800;color:var(--white);letter-spacing:1px}
.hero-sub{left:0;width:1200px;top:350px;font-size:16.5px;line-height:27px;color:var(--white)}
.btn{background:var(--blue);color:var(--white);font-weight:500;text-align:center;text-transform:uppercase}
.hero-btn{left:506px;top:425px;width:187px;height:56px;line-height:56px;font-size:20px}

/* welcome */
.eyebrow{color:var(--blue);font-size:16px}
.welcome-eyebrow{left:100px;top:853px}
.welcome-title{left:100px;top:890px;font-size:40px;font-weight:600;color:var(--ink)}
.welcome-sub{left:100px;top:944px;font-size:20px;font-weight:500;color:var(--ink)}
.welcome-copy{left:100px;top:993px;width:430px;font-size:14.5px;line-height:27px}
.welcome-copy p+p{margin-top:18px}
.welcome-btn{left:98px;top:1220px;width:187px;height:57px;line-height:57px;font-size:20px}
.welcome-media{left:584px;top:805px;width:528px;height:518px;background:radial-gradient(circle at 50% 55%,#6e7585 0%,#3d4458 55%,#262c3c 100%);clip-path:polygon(50% 0,100% 50%,50% 100%,0 50%)}

/* projects */
.projects-bg{left:0;top:1395px;width:1200px;height:990px;background:var(--grey-bg)}
.section-title{left:0;width:1200px;font-size:40px;font-weight:600;color:var(--ink)}
.section-eyebrow{left:0;width:1200px}
.projects-copy{left:0;width:1200px;top:1558px;font-size:15px;line-height:27px}
.project{top:1651px;height:385px}
.project-a{left:0;width:292px;background:linear-gradient(180deg,#8aa0b0 0%,#3f6a4a 40%,#4b6a86 75%,#2c3c58 100%)}
.project-b{left:314px;width:572px;background:linear-gradient(180deg,#5a5f6a 0%,#bcbfc4 45%,#eceef0 100%)}
.project-c{left:907px;width:293px;background:linear-gradient(150deg,#9fc4e8 0%,#dfe8f2 40%,#3a78d0 100%)}
.slider-nav{left:550px;top:2010px;width:98px;height:50px;background:var(--white);display:flex;align-items:center;justify-content:space-around}

/* contact form */
.form-box{left:230px;top:2141px;width:740px;height:505px;background:linear-gradient(100deg,#1a35c4 0%,#2b62e6 60%,#3a82f0 100%)}
.form-title{left:0;width:740px;top:54px;font-size:40px;font-weight:500;color:var(--white)}
.form-sub{left:0;width:740px;top:116px;font-size:15px;color:var(--white)}
.field{background:rgba(255,255,255,.1);color:var(--white);font-size:13px;padding:0 16px;line-height:52px;height:52px;width:328px}
.field.message{width:667px;height:83px;line-height:22px;padding-top:12px}
.submit{left:292px;top:387px;width:156px;height:57px;line-height:55px;border:1.5px solid var(--white);color:var(--white);font-size:19px;font-weight:500;text-align:center}

/* partners */
.partner-photo{top:2876px;height:260px;width:229px}
.partner-name{font-size:17px;font-weight:500;color:var(--ink);width:229px;text-align:center}
.partner-role{font-size:14px;width:229px;text-align:center;color:var(--muted)}
.partner-feature{left:485px;top:2876px;width:229px;height:355px;background:var(--white);box-shadow:0 6px 20px rgba(0,0,0,.08)}
.partner-arrow{left:642px;top:3094px;width:72px;height:44px;background:var(--blue);display:flex;align-items:center;justify-content:center}
.dots{left:566px;top:3272px;display:flex;gap:6px}
.dots span{width:18px;height:3px;background:#c7cbd3}
.dots span.on{background:var(--blue)}

/* cta */
.cta{left:0;top:3338px;width:1200px;height:395px;background:linear-gradient(180deg,#3f66e6 0%,#2a50d4 60%,#1f3fb8 100%)}
.cta-title{left:0;width:1200px;top:88px;font-size:40px;line-height:52px;font-weight:500;color:var(--white)}
.phone-pill{left:468px;top:230px;width:264px;height:58px;border-radius:29px;background:#0a0a0a;display:flex;align-items:center;gap:22px;padding-left:8px;color:var(--white);font-size:24px;font-weight:500}
.phone-pill .icon{width:44px;height:44px;border-radius:50%;background:var(--blue);border:3px solid var(--white);display:flex;align-items:center;justify-content:center}

/* footer */
.footer{left:0;top:3733px;width:1200px;height:345px;background:var(--footer);color:var(--white)}
.footer h4{font-size:17px;font-weight:500;text-transform:uppercase}
.footer-list{list-style:none;font-size:14px;line-height:29.5px}
.footer-list li::before{content:"";display:inline-block;width:6px;height:6px;border-radius:50%;background:var(--blue);margin-right:14px;vertical-align:middle}
.contact-row{display:flex;gap:12px;font-size:14.5px;line-height:27px;align-items:flex-start}
.news-copy{font-size:14px;line-height:27px}
.news-input{left:612px;top:165px;width:245px;height:50px;background:var(--white);color:#666;font-size:13px;padding-left:16px;line-height:50px}
.news-send{left:810px;top:172px;width:38px;height:36px;background:var(--blue);display:flex;align-items:center;justify-content:center}
.footer-rule{left:79px;top:274px;width:1042px;height:1px;background:#2a2a2a}
.copyright{left:0;width:1200px;top:298px;font-size:14px}
.copyright span{color:var(--blue)}
</style>
</head>
<body>

<!-- hero -->
<section class="abs hero" role="img" aria-label="Wind turbines above a lake with floating solar panels at dusk"></section>
<svg class="abs hero-cut" width="1200" height="140" viewBox="0 0 1200 140">
  <polygon points="0,40 600,131 1200,40 1200,140 0,140" fill="#ffffff"/>
  <polygon points="495,110 600,131 705,110 705,114 600,135 495,114" fill="#1f4fd8"/>
  <rect x="593" y="65" width="14" height="26" rx="7" fill="none" stroke="#1f4fd8" stroke-width="2"/>
  <line x1="600" y1="71" x2="600" y2="77" stroke="#1f4fd8" stroke-width="2"/>
</svg>
<div class="abs brand" style="left:80px;top:32px"><span class="dot"></span>Marlowfield Equity Partners</div>
<nav class="abs nav">
  <span class="active">HOME</span><span>ABOUT US</span><span>PARTNERS</span><span>PROJECTS</span><span>CONTACT</span>
  <svg width="20" height="20" viewBox="0 0 20 20"><circle cx="8" cy="8" r="6" fill="none" stroke="#fff" stroke-width="2"/><line x1="12.5" y1="12.5" x2="18" y2="18" stroke="#fff" stroke-width="2"/></svg>
</nav>
<h1 class="abs hero-title center">FOREIGN INVESTMENT</h1>
<p class="abs hero-sub center">We Work with Energy and Healthcare to Raise Foreign Capital<br>For Projects</p>
<div class="abs btn hero-btn">Contact Us</div>

<!-- welcome -->
<p class="abs eyebrow welcome-eyebrow">Welcome To</p>
<h2 class="abs welcome-title">MARLOWFIELD</h2>
<p class="abs welcome-sub">EQUITY PARTNERS</p>
<div class="abs welcome-copy">
  <p>Lorem Ipsum is simply dummy text of the printing and typesetting industry &nbsp;Lorem Ipsum.</p>
  <p>Lorem Ipsum is simply dummy text of the printing and typesetting industry. Lorem Ipsum has been the industry standard dummy text ever since the 1500s when an unknown printer took a galley Lorem Ipsum is simply dummy text of the printing.</p>
</div>
<div class="abs btn welcome-btn">Learn More</div>
<div class="abs welcome-media" role="img" aria-label="Business handshake photograph"></div>

<!-- projects -->
<section class="abs projects-bg"></section>
<p class="abs eyebrow section-eyebrow center" style="top:1472px">Completed</p>
<h2 class="abs section-title center" style="top:1500px">OUR PROJECTS</h2>
<p class="abs projects-copy center">Lorem Ipsum is simply dummy text of the printing and typesetting<br>industry &nbsp;Lorem Ipsum Lorem Ipsum is simply</p>
<div class="abs project project-a" role="img" aria-label="Hillside reservoir with floating solar array"></div>
<div class="abs project project-b" role="img" aria-label="Businessman signing a contract beside a model house"></div>
<div class="abs project project-c" role="img" aria-label="Medical chart with stethoscope and laptop"></div>
<div class="abs slider-nav">
  <svg width="12" height="20" viewBox="0 0 12 20"><polyline points="10,2 2,10 10,18" fill="none" stroke="#555" stroke-width="1.6"/></svg>
  <svg width="12" height="20" viewBox="0 0 12 20"><polyline points="2,2 10,10 2,18" fill="none" stroke="#1f4fd8" stroke-width="1.8"/></svg>
</div>

<!-- contact form -->
<section class="abs form-box">
  <h2 class="abs form-title center">Keep In Touch</h2>
  <p class="abs form-sub center">If you have an any Question for Contact Us Today !</p>
  <div class="abs field" style="left:36px;top:159px">Name *</div>
  <div class="abs field" style="left:375px;top:159px">Phone *</div>
  <div class="abs field" style="left:36px;top:221px">Email *</div>
  <div class="abs field" style="left:375px;top:221px">Projects *</div>
  <div class="abs field message" style="left:36px;top:283px">Message *</div>
  <div class="abs submit">SUBMIT</div>
</section>

<!-- partners -->
<p class="abs eyebrow section-eyebrow center" style="top:2718px">Meet</p>
<h2 class="abs section-title center" style="top:2745px">OUR PARTNER</h2>
<div class="abs partner-feature"></div>
<div class="abs partner-photo" style="left:-16px;background:linear-gradient(180deg,#c9c4bd,#a79e94)" role="img" aria-label="Portrait of a partner"></div>
<div class="abs partner-photo" style="left:233px;background:linear-gradient(180deg,#c5ccd2,#3d4452)" role="img" aria-label="Portrait of a partner"></div>
<div class="abs partner-photo" style="left:485px;background:linear-gradient(180deg,#8f8a84,#3e5370)" role="img" aria-label="Portrait of a partner"></div>
<div class="abs partner-photo" style="left:737px;background:linear-gradient(180deg,#dcdcdc,#b4b0aa)" role="img" aria-label="Portrait of a partner"></div>
<div class="abs partner-photo" style="left:987px;width:229px;background:linear-gradient(180deg,#bfc3c8,#2a2d33)" role="img" aria-label="Portrait of a partner"></div>
<div class="abs partner-arrow"><svg width="40" height="14" viewBox="0 0 40 14"><line x1="2" y1="7" x2="36" y2="7" stroke="#fff" stroke-width="1.5"/><polyline points="30,1 37,7 30,13" fill="none" stroke="#fff" stroke-width="1.5"/></svg></div>
<p class="abs partner-name" style="left:-8px;top:3158px">PARTNER NAME</p>
<p class="abs partner-role" style="left:-8px;top:3185px">Lorem Ipsum text</p>
<p class="abs partner-name" style="left:228px;top:3158px">PARTNER NAME</p>
<p class="abs partner-role" style="left:228px;top:3185px">Lorem Ipsum text</p>
<p class="abs partner-name" style="left:485px;top:3162px">PARTNER NAME</p>
<p class="abs partner-role" style="left:485px;top:3189px">Lorem Ipsum text</p>
<p class="abs partner-name" style="left:740px;top:3158px">PARTNER NAME</p>
<p class="abs partner-role" style="left:740px;top:3185px">Lorem Ipsum text</p>
<p class="abs partner-name" style="left:994px;top:3158px">PARTNER NAME</p>
<p class="abs partner-role" style="left:994px;top:3185px">Lorem Ipsum text</p>
<div class="abs dots"><span class="on"></span><span></span><span></span></div>

<!-- cta -->
<section class="abs cta" role="img" aria-label="City skyline behind a businessman, tinted blue">
  <h2 class="abs cta-title center">If youHave an any Question for<br>Contact Us Today !</h2>
  <div class="abs phone-pill">
    <span class="icon"><svg width="20" height="20" viewBox="0 0 24 24"><path d="M6.6 10.8a15 15 0 006.6 6.6l2.2-2.2c.3-.3.7-.4 1-.2 1.1.4 2.3.6 3.6.6.6 0 1 .4 1 1V20c0 .6-.4 1-1 1A17 17 0 013 4c0-.6.4-1 1-1h3.5c.6 0 1 .4 1 1 0 1.3.2 2.5.6 3.6.1.3 0 .7-.2 1z" fill="#fff"/></svg></span>
    123 456 7890
  </div>
</section>

<!-- footer -->
<footer class="abs footer">
  <h4 class="abs" style="left:79px;top:42px">Sitemap</h4>
  <ul class="abs footer-list" style="left:79px;top:92px">
    <li>Home</li><li>About Us</li><li>Partners</li><li>Projects</li><li>Contact</li>
  </ul>
  <h4 class="abs" style="left:346px;top:42px">Contact Us</h4>
  <div class="abs" style="left:344px;top:90px;display:flex;flex-direction:column;gap:12px">
    <div class="contact-row"><svg width="18" height="26" viewBox="0 0 18 26"><path d="M9 1a8 8 0 00-8 8c0 6 8 15 8 15s8-9 8-15a8 8 0 00-8-8z" fill="none" stroke="#1f4fd8" stroke-width="2"/><circle cx="9" cy="9" r="3" fill="#1f4fd8"/></svg><span>Lorem ipsum simple<br>text print text.</span></div>
    <div class="contact-row"><svg width="20" height="20" viewBox="0 0 24 24"><path d="M6.6 10.8a15 15 0 006.6 6.6l2.2-2.2c.3-.3.7-.4 1-.2 1.1.4 2.3.6 3.6.6.6 0 1 .4 1 1V20c0 .6-.4 1-1 1A17 17 0 013 4c0-.6.4-1 1-1h3.5c.6 0 1 .4 1 1 0 1.3.2 2.5.6 3.6.1.3 0 .7-.2 1z" fill="#1f4fd8"/></svg><span>123 456 7890</span></div>
    <div class="contact-row"><svg width="20" height="16" viewBox="0 0 20 16"><rect x="0" y="1" width="20" height="14" fill="#1f4fd8"/><polyline points="0,1 10,9 20,1" fill="none" stroke="#080808" stroke-width="1.5"/></svg><span>info@marlowfield.com</span></div>
  </div>
  <h4 class="abs" style="left:612px;top:42px">Newsletter</h4>
  <p class="abs news-copy" style="left:612px;top:98px">Would you like to receive our<br>exclusive update for signup !</p>
  <div class="abs news-input">Enter Email *</div>
  <div class="abs news-send"><svg width="20" height="18" viewBox="0 0 20 18"><polygon points="1,8 19,1 14,17 9,11" fill="none" stroke="#fff" stroke-width="1.5"/><line x1="9" y1="11" x2="19" y2="1" stroke="#fff" stroke-width="1.5"/></svg></div>
  <div class="abs brand" style="left:884px;top:62px;font-size:20px;gap:10px"><span class="dot" style="width:14px;height:14px"></span>Marlowfield<br>Equity Partners</div>
  <div class="abs footer-rule"></div>
  <p class="abs copyright center">©<span>MARLOWFIELD EQUITY PARTNERS</span> - 2020 All rights reserved.</p>
</footer>

</body>
</html>
```